Podcast Cover Art Design for Divorce Support

Need a podcast cover art design for new podcast that will cover Emotional Divorce Support and Recovery topics. People are lost, confused. They are looking for help during the confusion and heartbreak. Main Title is "Quiet Harbor Podcast". Subtitle is "How to Let Go and Move On". We want a design that is encouraging yet not overly "happy". We also want to convey kindness, clarity, and strength, if possible. Our logo colors use grey and red though we aren't tied to those colors for the podcast. Logo may be used on the podcast but not required. Final image should be 3000x3000px. Our logo uses Montserrat-Medium and Multi-SemiBold. Not necessary but available if you want to use it.

```html
<!DOCTYPE html>
<html lang="en">
<head>
<meta charset="utf-8">
<title>Quiet Harbor Podcast – Cover Art</title>
<link rel="stylesheet" href="https://fonts.googleapis.com/css2?family=Montserrat:wght@800;900&display=swap">
<style>
  :root {
    --page-bg: #ffffff;
    --sky-top: #3f86c8;
    --sky-mid: #a9d0ee;
    --horizon: #d8ecf8;
    --sea-top: #4a93cf;
    --sea-deep: #1b4f95;
    --heart-red: #c8202a;
    --title-red: #e30613;
    --title-red-shadow: #7d0a10;
    --title-grey: #555558;
    --title-grey-shadow: #2a2a2c;
    --subtitle-white: #ffffff;
    --subtitle-shadow: #0c1f3a;
  }
  html, body {
    margin: 0;
    padding: 0;
    width: 1200px;
    height: 1000px;
    overflow: hidden;
    background: var(--page-bg);
  }
  .canvas {
    position: relative;
    width: 1200px;
    height: 1000px;
    font-family: "Montserrat", Arial, sans-serif;
  }
  .cover {
    position: absolute;
    left: 170px;
    top: 68px;
    width: 862px;
    height: 862px;
    overflow: hidden;
  }
  .cover-scene {
    position: absolute;
    inset: 0;
    background:
      radial-gradient(ellipse 300px 260px at 50% 62%, rgba(200,32,42,0.75), rgba(200,32,42,0) 70%),
      linear-gradient(180deg, var(--sky-top) 0%, var(--sky-mid) 35%, var(--horizon) 55%, var(--sea-top) 56%, var(--sea-deep) 100%);
  }
  .title {
    position: absolute;
    left: 0;
    width: 100%;
    margin: 0;
    text-align: center;
    font-weight: 900;
    line-height: 1;
    letter-spacing: -1px;
  }
  .title-primary {
    top: 30px;
    font-size: 138px;
    color: var(--title-red);
    text-shadow: 4px 5px 0 var(--title-red-shadow);
    z-index: 2;
  }
  .title-secondary {
    top: 162px;
    font-size: 134px;
    color: var(--title-grey);
    text-shadow: 3px 4px 0 var(--title-grey-shadow);
    z-index: 1;
  }
  .format-label {
    position: absolute;
    left: 414px;
    top: 296px;
    writing-mode: vertical-rl;
    transform: rotate(180deg);
    font-weight: 900;
    font-size: 62px;
    line-height: 1;
    letter-spacing: 1px;
  }
  .format-label .pod { color: var(--title-grey); }
  .format-label .cast { color: var(--title-red); }
  .brand {
    position: absolute;
    left: 0;
    width: 100%;
    top: 692px;
    display: flex;
    justify-content: center;
    align-items: center;
    gap: 8px;
  }
  .brand-dot {
    width: 18px;
    height: 18px;
    border-radius: 50%;
    background: var(--title-red);
  }
  .brand-name {
    font-weight: 800;
    font-size: 20px;
    color: var(--title-red);
  }
  .subtitle {
    position: absolute;
    left: 0;
    width: 100%;
    top: 790px;
    margin: 0;
    text-align: center;
    font-weight: 900;
    font-size: 36px;
    color: var(--subtitle-white);
    text-shadow: 2px 3px 0 var(--subtitle-shadow);
    letter-spacing: 0.5px;
  }
</style>
</head>
<body>
  <div class="canvas">
    <section class="cover">
      <div class="cover-scene" role="img" aria-label="Sky with clouds over the sea, a broken red heart split in two halves floating in the water, each half with a small figure rowing with an oar"></div>
      <h1 class="title title-primary">QUIET</h1>
      <h1 class="title title-secondary">HARBOR</h1>
      <div class="format-label"><span class="pod">POD</span><span class="cast">CAST</span></div>
      <div class="brand">
        <span class="brand-dot"></span>
        <span class="brand-name">Harborline</span>
      </div>
      <p class="subtitle">HOW TO LET GO AND MOVE ON</p>
    </section>
  </div>
</body>
</html>
```